Keystone Institute Logo & Business card

Keystone Institute - Professional ICT Training
business is a training center.
Logo and business card that have an ID.
bold publicity, distinct, and prestige image
"Ensure professional Success"
that will attract target customer to come and take a look. that will look prestige on certificate after graduation, that will serve as a business tool to attract Business and enterprise customer (let them send their staff for training)

Target Market(s)

young professionals, university students, youth building career in IT fields

Industry/Entity Type

Education

Contact Information for Business Card

Font styles to use
Sans Serif

Colors

Designer to choose colors to be used in the design.

Requirements
Must have
• Logo Identity
• uniqueness
Nice to have
• catch phrase or illustration
Should not have
• just use alphabet as logo.

```html
<!DOCTYPE html>
<html lang="en">
<head>
<meta charset="utf-8">
<title>Keystone Institute – Business Card</title>
<link rel="stylesheet" href="https://fonts.googleapis.com/css2?family=Montserrat:wght@700&family=Roboto:wght@500&family=Work+Sans:wght@400;600&display=swap">
<style>
  :root {
    --stage: #1f1f1f;
    --paper: #ffffff;
    --navy: #20447a;
    --sky: #29a8e0;
    --ink: #4a4a4a;
  }
  * { box-sizing: border-box; margin: 0; padding: 0; }
  html, body { width: 1200px; height: 900px; overflow: hidden; }
  body {
    background: var(--stage);
    position: relative;
    font-family: "Work Sans", sans-serif;
  }
  .card {
    position: absolute;
    left: 261px;
    width: 656px;
    height: 358px;
  }
  .card--front { top: 69px; background: var(--paper); }
  .card--back {
    top: 472px;
    background: var(--navy);
    display: flex;
    align-items: center;
    justify-content: center;
  }

  .brand { display: flex; align-items: center; }
  .brand__mark { flex: none; }
  .brand__name {
    font-family: "Montserrat", sans-serif;
    font-weight: 700;
    letter-spacing: 0.04em;
    white-space: nowrap;
  }
  .card--front .brand {
    position: absolute;
    left: 35px;
    top: 159px;
    height: 40px;
  }
  .card--front .brand__mark { width: 40px; height: 40px; background: var(--navy); }
  .card--front .brand__name { margin-left: 14px; font-size: 19px; color: var(--navy); }

  .card--back .brand { margin-bottom: 4px; }
  .card--back .brand__mark { width: 57px; height: 57px; background: var(--sky); }
  .card--back .brand__name { margin-left: 16px; font-size: 30px; color: var(--paper); }

  .divider {
    position: absolute;
    left: 364px;
    top: 83px;
    width: 2px;
    height: 193px;
    background: var(--navy);
  }

  .contact {
    position: absolute;
    left: 399px;
    top: 76px;
    color: var(--ink);
  }
  .contact__name {
    font-family: "Roboto", sans-serif;
    font-weight: 500;
    font-size: 27px;
    line-height: 30px;
    color: var(--navy);
    letter-spacing: 0.01em;
  }
  .contact__role { font-size: 16px; line-height: 20px; margin-top: 1px; letter-spacing: 0.03em; }
  .contact__address { font-size: 16px; line-height: 22px; margin-top: 10px; letter-spacing: 0.04em; }
  .contact__list { list-style: none; margin-top: 8px; }
  .contact__item {
    display: flex;
    align-items: center;
    font-size: 16px;
    line-height: 22px;
    letter-spacing: 0.04em;
  }
  .contact__icon { width: 11px; height: 11px; margin-right: 7px; flex: none; }
  .contact__strong { font-weight: 600; color: var(--navy); }
</style>
</head>
<body>
  <section class="card card--front">
    <div class="brand">
      <span class="brand__mark"></span>
      <span class="brand__name">KEYSTONE INSTITUTE</span>
    </div>

    <span class="divider"></span>

    <div class="contact">
      <h1 class="contact__name">DANA WHITFIELD</h1>
      <p class="contact__role">Director</p>
      <p class="contact__address">48 Harbor Lane<br>Easton, MA 02375</p>
      <ul class="contact__list">
        <li class="contact__item">
          <svg class="contact__icon" viewBox="0 0 12 12" aria-hidden="true"><path d="M2.5 1 L4.5 1 L5 3.5 L3.8 4.4 Q4.8 6.8 7.4 8.2 L8.4 7 L11 7.6 L11 9.6 Q10.6 11 9 11 Q1 9.6 1 2.6 Q1 1.2 2.5 1 Z" fill="#20447a"/></svg>
          555-201-0148
        </li>
        <li class="contact__item">
          <svg class="contact__icon" viewBox="0 0 12 12" aria-hidden="true"><rect x="2.5" y="0.8" width="7" height="10.4" rx="1.2" fill="none" stroke="#20447a" stroke-width="1.4"/><rect x="5" y="8.6" width="2" height="1.2" fill="#20447a"/></svg>
          555-201-0149
        </li>
        <li class="contact__item">
          <svg class="contact__icon" viewBox="0 0 12 12" aria-hidden="true"><rect x="0.8" y="2.3" width="10.4" height="7.4" rx="1" fill="none" stroke="#20447a" stroke-width="1.3"/><path d="M1 2.8 L6 6.6 L11 2.8" fill="none" stroke="#20447a" stroke-width="1.2"/></svg>
          info@keystoneinstitute.com
        </li>
        <li class="contact__item">
          <svg class="contact__icon" viewBox="0 0 12 12" aria-hidden="true"><g fill="none" stroke="#20447a" stroke-width="0.9"><circle cx="6" cy="6" r="5.2"/><ellipse cx="6" cy="6" rx="2.3" ry="5.2"/><path d="M0.8 6 H11.2 M1.6 3.4 H10.4 M1.6 8.6 H10.4"/></g></svg>
          <span>www.<span class="contact__strong">keystoneinstitute</span>.com</span>
        </li>
      </ul>
    </div>
  </section>

  <section class="card card--back">
    <div class="brand">
      <span class="brand__mark"></span>
      <span class="brand__name">KEYSTONE INSTITUTE</span>
    </div>
  </section>
</body>
</html>
```